Need Business Card for our Indian Grocery Store

Industry/Entity Type

Grocery Store

Contact Information for Business Card

Manoj Baweja
Director

Store Locations:

Kelbridge
482 Elm Parade
P: 03 9172 5843

Larkfield
613 Carlow Road
P: 03 9238 6014

email: kvtmarts@mailnest.example

Requirements
Must have
• Our logo Colours

```html
<!DOCTYPE html>
<html lang="en">
<head>
<meta charset="utf-8">
<title>KVT Groceries &amp; Spices – Business Card</title>
<link href="https://fonts.googleapis.com/css2?family=Fira+Sans:ital,wght@0,400;0,500;0,600;0,700;1,700&family=Fjalla+One&display=swap" rel="stylesheet">
<style>
  :root {
    --brand-red: #d2161c;
    --brand-red-deep: #c11217;
    --card-white: #ffffff;
    --ink-grey: #4a4a4a;
    --canvas-bg: #e8e5e1;
  }
  html, body {
    margin: 0;
    padding: 0;
    width: 1200px;
    height: 1200px;
    overflow: hidden;
    background: var(--canvas-bg);
  }
  .card {
    position: absolute;
    left: 229px;
    width: 734px;
    height: 408px;
    border-radius: 32px;
    box-shadow: 0 10px 24px rgba(0,0,0,0.22);
    overflow: hidden;
    font-family: "Fira Sans", sans-serif;
  }
  .card-front { top: 158px; background: var(--card-white); }
  .card-back { top: 646px; background: var(--brand-red); }

  /* Front */
  .brand-name {
    position: absolute;
    left: 59px;
    top: 160px;
    width: 315px;
    margin: 0;
    display: flex;
    align-items: center;
    gap: 10px;
    white-space: nowrap;
    color: var(--brand-red);
    font-weight: 700;
    font-size: 23px;
    line-height: 1.1;
  }
  .brand-mark {
    flex: none;
    width: 34px;
    height: 34px;
    background: var(--brand-red);
    border-radius: 6px;
  }
  .locations-title {
    position: absolute;
    left: 393px;
    top: 140px;
    width: 283px;
    height: 36px;
    margin: 0;
    background: var(--brand-red);
    border-radius: 6px;
    color: var(--card-white);
    font-family: "Fjalla One", sans-serif;
    font-weight: 400;
    font-size: 23px;
    letter-spacing: 4px;
    line-height: 36px;
    text-align: center;
  }
  .store {
    position: absolute;
    top: 186px;
    width: 170px;
    text-align: center;
    font-size: 18px;
    line-height: 28px;
    color: var(--ink-grey);
  }
  .store-first { left: 370px; }
  .store-second { left: 528px; }
  .store-town { color: var(--brand-red); }
  .store-phone svg {
    width: 14px;
    height: 14px;
    vertical-align: -1px;
    margin-right: 4px;
    fill: var(--brand-red);
  }
  .tagline {
    position: absolute;
    left: 0;
    right: 0;
    top: 338px;
    margin: 0;
    display: flex;
    justify-content: center;
    align-items: center;
    gap: 8px;
    color: var(--brand-red);
    font-style: italic;
    font-weight: 700;
    font-size: 19px;
  }
  .tagline::before, .tagline::after {
    content: "";
    width: 30px;
    height: 2px;
    background: var(--brand-red);
  }

  /* Back */
  .back-pattern {
    position: absolute;
    inset: 0;
    background: radial-gradient(circle at 50% 50%, var(--brand-red) 0%, var(--brand-red-deep) 100%);
  }
  .name-frame {
    position: absolute;
    left: 191px;
    top: 106px;
    width: 352px;
    height: 152px;
    box-sizing: border-box;
    background: var(--card-white);
    border-radius: 28px;
    box-shadow: inset 0 0 0 6px var(--card-white), inset 0 0 0 9px var(--brand-red);
    text-align: center;
    color: var(--brand-red);
  }
  .person-name {
    margin: 0;
    padding-top: 48px;
    font-weight: 600;
    font-size: 33px;
    line-height: 40px;
    letter-spacing: -0.5px;
  }
  .person-title {
    margin: 0;
    font-weight: 600;
    font-size: 20px;
    line-height: 24px;
  }
  .email-bar {
    position: absolute;
    left: 201px;
    top: 264px;
    width: 334px;
    height: 42px;
    background: var(--card-white);
    border-radius: 0 0 8px 8px;
    color: var(--brand-red);
    font-weight: 500;
    font-size: 16px;
    letter-spacing: 1.5px;
    line-height: 42px;
    text-align: center;
    white-space: nowrap;
  }
</style>
</head>
<body>
  <section class="card card-front">
    <h1 class="brand-name"><span class="brand-mark"></span><span>KVT Groceries &amp; Spices</span></h1>

    <h2 class="locations-title">STORE LOCATIONS</h2>

    <div class="store store-first">
      <div class="store-town">Kelbridge</div>
      <div class="store-address">482 Elm Parade</div>
      <div class="store-phone"><svg viewBox="0 0 24 24" aria-hidden="true"><path d="M6.6 10.8a15.1 15.1 0 0 0 6.6 6.6l2.2-2.2c.3-.3.7-.4 1-.2 1.1.4 2.3.6 3.6.6.6 0 1 .4 1 1V20c0 .6-.4 1-1 1C10.6 21 3 13.4 3 4c0-.6.4-1 1-1h3.5c.6 0 1 .4 1 1 0 1.3.2 2.5.6 3.6.1.3 0 .7-.2 1z"/></svg>03 9172 5843</div>
    </div>

    <div class="store store-second">
      <div class="store-town">Larkfield</div>
      <div class="store-address">613 Carlow Road</div>
      <div class="store-phone"><svg viewBox="0 0 24 24" aria-hidden="true"><path d="M6.6 10.8a15.1 15.1 0 0 0 6.6 6.6l2.2-2.2c.3-.3.7-.4 1-.2 1.1.4 2.3.6 3.6.6.6 0 1 .4 1 1V20c0 .6-.4 1-1 1C10.6 21 3 13.4 3 4c0-.6.4-1 1-1h3.5c.6 0 1 .4 1 1 0 1.3.2 2.5.6 3.6.1.3 0 .7-.2 1z"/></svg>03 9238 6014</div>
    </div>

    <p class="tagline">Trusted Name Since 2008</p>
  </section>

  <section class="card card-back">
    <div class="back-pattern" role="img" aria-label="Subtle red mandala pattern covering the card back"></div>
    <div class="name-frame">
      <p class="person-name">Manoj Baweja</p>
      <p class="person-title">Director</p>
    </div>
    <div class="email-bar">kvtmarts@mailnest.example</div>
  </section>
</body>
</html>
```